Construction company focused on concrete and shed construction.

We need to update our current business card for ridgeforgebuilds.com.au we would like an eye catching design with blue, grey and white incorporating our current logo.
Our company started off in concreting and due to varying factors we have expanded to include shed construction as well.
This has led to our current Logo looking a little out of place and somehow need to use the card to bring in the shed construction side of the business while not having to change current concrete look "KESTRO" logo as we already have this incorporated into our company clothing and are not willing to change this yet.
Photo image attached for inspiration/ visual reference of type of work, not to be used on final design.
Please no cheesy designs of men in hard hats and tools
Final design should demonstrate a modern and service focused company.

Target Market(s)

Farmers, Business owners, Developers, Architects, Commercial project delivery

Industry/Entity Type

Construction Company

Contact Information for Business Card

Kestro Constructions.
7b Harlow st
Corvale Heights
03 62918873

Font styles to use
Other font styles liked:
• see font in logo

Colors
3176b5
b2b2b2

Requirements
Must have
• Easy to read font,
• good contrast between back ground and writing
Nice to have
• Modern and corporate look with a fun but professional image.
Should not have
• Comic images or shadow images of tools/ people.

```html
<!DOCTYPE html>
<html lang="en">
<head>
<meta charset="utf-8">
<title>Kestro Constructions – Business Card</title>
<link rel="stylesheet" href="https://fonts.googleapis.com/css2?family=Montserrat:wght@400;500;600&family=Oswald:wght@500&display=swap">
<style>
  :root {
    --brand-blue: #3176b5;
    --brand-grey: #b2b2b2;
    --ink: #2b2b2b;
    --ink-soft: #555;
    --paper: #ffffff;
    --backdrop: #e9ecef;
  }
  * { box-sizing: border-box; margin: 0; padding: 0; }
  html, body {
    width: 1200px; height: 738px; overflow: hidden;
    background: var(--backdrop);
    font-family: "Montserrat", Arial, sans-serif;
  }
  .sheet {
    position: relative; width: 1200px; height: 738px;
    display: flex; align-items: center; justify-content: center; gap: 50px;
  }
  .card {
    position: relative; width: 540px; height: 310px; overflow: hidden;
    border-radius: 3px;
    box-shadow: 0 6px 18px rgba(0,0,0,.14);
  }

  /* Front */
  .card--front {
    background: var(--brand-blue);
    display: flex; flex-direction: column; align-items: center; justify-content: center;
  }
  .brand-mark { display: flex; align-items: center; gap: 10px; }
  .brand-mark__dot { width: 34px; height: 34px; border-radius: 50%; }
  .brand-mark__name {
    font-family: "Oswald", "Arial Narrow", sans-serif;
    font-weight: 500; letter-spacing: 3px;
  }
  .card--front .brand-mark__dot { background: var(--paper); }
  .card--front .brand-mark__name { color: var(--paper); font-size: 34px; }
  .company-name {
    margin-top: 38px;
    font-family: "Oswald", "Arial Narrow", sans-serif;
    font-weight: 500; font-size: 27px; letter-spacing: .5px;
    color: var(--paper); text-transform: uppercase;
  }

  /* Back */
  .card--back { background: var(--paper); }
  .card--back .brand-mark { position: absolute; left: 60px; top: 118px; }
  .card--back .brand-mark__dot { background: var(--brand-grey); }
  .card--back .brand-mark__name { color: var(--brand-blue); font-size: 30px; }
  .divider {
    position: absolute; left: 268px; top: 52px; width: 2px; height: 128px;
    background: var(--brand-blue);
  }
  .contact { position: absolute; left: 296px; top: 44px; }
  .contact__name {
    font-size: 21px; font-weight: 600; color: var(--brand-blue); letter-spacing: .3px;
  }
  .contact__role { font-size: 12px; color: var(--ink); margin-top: 1px; }
  .contact__address {
    margin-top: 14px; font-size: 12.5px; line-height: 1.35; color: var(--ink-soft);
  }
  .contact__lines { list-style: none; margin-top: 10px; }
  .contact__line {
    display: flex; align-items: center; gap: 9px;
    font-size: 13px; color: var(--ink); line-height: 1.4;
  }
  .contact__line svg { width: 10px; height: 10px; fill: var(--brand-blue); flex: none; }
  .contact__accent { color: var(--brand-blue); }
  .wave { position: absolute; left: 0; bottom: 0; width: 540px; height: 100px; }
</style>
</head>
<body>
<main class="sheet">

  <section class="card card--front" aria-label="Card front">
    <div class="brand-mark">
      <span class="brand-mark__dot"></span>
      <span class="brand-mark__name">KESTRO</span>
    </div>
    <h1 class="company-name">Kestro Constructions.</h1>
  </section>

  <section class="card card--back" aria-label="Card back">
    <div class="brand-mark">
      <span class="brand-mark__dot"></span>
      <span class="brand-mark__name">KESTRO</span>
    </div>

    <div class="divider"></div>

    <div class="contact">
      <h2 class="contact__name">Marcus Hale</h2>
      <p class="contact__role">Director</p>
      <p class="contact__address">7b Harlow st<br>Corvale Heights</p>
      <ul class="contact__lines">
        <li class="contact__line">
          <svg viewBox="0 0 10 10" aria-hidden="true"><path d="M2 .5l1.6 2-1 1.1c.6 1.3 1.5 2.2 2.8 2.8l1.1-1 2 1.6-1 1.8C4.4 8.6 1.4 5.6.3 1.5z"/></svg>
          03 62918873
        </li>
        <li class="contact__line">
          <svg viewBox="0 0 10 10" aria-hidden="true"><path d="M0 2h10v6H0z M0 2l5 3.3L10 2" fill="none" stroke="#3176b5" stroke-width="1.2"/></svg>
          info@kestro.com
        </li>
        <li class="contact__line">
          <svg viewBox="0 0 10 10" aria-hidden="true"><circle cx="5" cy="5" r="4.3" fill="none" stroke="#3176b5" stroke-width="1.1"/><path d="M.7 5h8.6M5 .7c-2.4 2.6-2.4 6 0 8.6M5 .7c2.4 2.6 2.4 6 0 8.6" fill="none" stroke="#3176b5" stroke-width=".8"/></svg>
          <span>www.<span class="contact__accent">kestro</span>.com</span>
        </li>
      </ul>
    </div>

    <svg class="wave" viewBox="0 0 540 100" preserveAspectRatio="none" aria-hidden="true">
      <path d="M0 90 C120 102 200 66 300 36 C380 16 460 10 540 16 L540 100 L0 100 Z" fill="#b2b2b2"/>
      <path d="M0 95 C120 106 210 72 305 44 C385 24 465 18 540 24 L540 100 L0 100 Z" fill="#ffffff"/>
      <path d="M0 98 C120 108 215 77 310 50 C390 30 468 24 540 30 L540 100 L0 100 Z" fill="#3176b5"/>
    </svg>
  </section>

</main>
</body>
</html>
```